Young judge needs a website to publish and to connect

I would like to have a website where I can publish my articles in public law. I am judge at the Alpine Civic Review Tribunal. Therefore, the website must have a calm, friendly and fairly neutral design. Also, it should be mobile friendly and easy to use.

On my website, I want to

- publish articles such as https://www.brindlepost.example/pulse/how-win-court-tobias-wenger/ and get feedbacks from my colleagues
- generate interest for my project on 'Statutes and Society - Notes from the Chamber', a book that I would like to publish in 2020 and which brings together my publications on public law (http://www.civicnorm.example/content/english/profil/publikationen.html ).
- provide updates for my university courses on constitutional, administrative and international law.

For that purpose, I would kindly ask you to suggest a website that communicates a fresh approach to the work of a young judge in constitutional and administrative law. Please have in mind that I do not only sit on the bench, but that I also work in academia. Therefore, it should be suitable for an audience from both university and law practice. The website should replace the existing website on www.civicnorm.example that I designed when still working as a lawyer. Thank you.

Target Market(s)

Academica, law firms, courts

Industry/Entity Type

University

Contact Information for Business Card

Tobias Wenger
Judge
Alpine Civic Review Tribunal
M +41 79 5XX 8X 2X

Logo Text

Notes from the Chamber

Number of Pages Required

5+ page

Font styles to use
Sans Serif

Colors
0455a3

Requirements
Must have
• - a page where I can publish and get feedbacks
• - a page about my project on law and politics
• - a page where I can provide updates for my university courses on constitutional, administrative and international law
• - page where I can list current and planned projects
• - a collaborative, young and fresh approach
Nice to have
• - a page reserved for my colleagues at the Alpine Civic Review Tribunal where I can alert them about to possibility to collaborate (if possibly password protected) and where they may suggest what to contribute to a specific project
Should not have
• anything which might to suggest that I want to make money with it, bragging or pretentious. Do not forget: I am judge, not a barrister.

```html
<!DOCTYPE html>
<html lang="en">
<head>
<meta charset="utf-8">
<title>Public Law – Tobias Wenger</title>
<link href="https://fonts.googleapis.com/css2?family=Lato:wght@400;700;900&family=Fira+Sans:wght@300&display=swap" rel="stylesheet">
<style>
  :root {
    --blue: #0455a3;
    --bar: #141414;
    --ink: #3a3a3a;
    --footer: #000;
    --white: #fff;
    --nav-dim: #8a8a8a;
    --nav-light: #e6e6e6;
  }
  * { margin: 0; padding: 0; box-sizing: border-box; }
  html, body { width: 960px; height: 1200px; overflow: hidden; background: var(--white); }
  body { position: relative; font-family: "Lato", sans-serif; color: var(--ink); }

  .hero {
    position: absolute; left: 0; top: 0; width: 960px; height: 523px;
    background:
      radial-gradient(ellipse 300px 260px at 260px 330px, rgba(70,45,30,.55), transparent 70%),
      linear-gradient(100deg, #1c1511 0%, #2a211b 35%, #302a28 60%, #2a1f18 100%);
  }
  .hero-title {
    position: absolute; left: 0; width: 960px; top: 212px; text-align: center;
    font-weight: 900; font-size: 62px; letter-spacing: 4px; color: var(--white);
  }
  .hero-rule { position: absolute; left: 278px; top: 291px; width: 403px; height: 2px; background: var(--blue); }

  .topbar { position: absolute; left: 0; top: 0; width: 960px; height: 72px; background: rgba(18,18,18,.96); }
  .topbar::after { content: ""; position: absolute; left: 0; top: 50px; width: 960px; height: 22px; background: rgba(10,10,10,.6); }
  .nav-link {
    position: absolute; top: 43px; font-size: 16px; letter-spacing: .3px; z-index: 2;
    text-transform: uppercase;
  }
  .nav-link.dim { color: var(--nav-dim); }
  .nav-link.light { color: var(--nav-light); }
  .brand { position: absolute; top: 12px; left: 376px; width: 200px; text-align: center; z-index: 2; }
  .brand-dot { display: block; width: 22px; height: 22px; border-radius: 50%; background: var(--blue); margin: 0 auto 4px; }
  .brand-name { font-size: 21px; color: #6e6e6e; }

  .copy {
    position: absolute; left: 0; width: 960px; text-align: center;
    font-family: "Fira Sans", sans-serif; font-weight: 300; font-size: 21px; line-height: 22.7px; color: var(--ink);
  }
  .section-title { position: absolute; left: 0; width: 960px; top: 807px; text-align: center; font-weight: 700; font-size: 33px; letter-spacing: 1px; color: var(--ink); }

  .load-more { position: absolute; left: 0; width: 960px; top: 1054px; text-align: center; font-weight: 700; font-size: 21px; color: #111; }
  .load-more svg { display: block; margin: 2px auto 0; }

  .footer { position: absolute; left: 0; top: 1125px; width: 960px; height: 75px; background: var(--footer); }
  .footer-note { position: absolute; left: 0; width: 945px; top: 24px; text-align: center; color: var(--white); font-weight: 700; font-size: 21px; }
  .social { position: absolute; top: 20px; width: 34px; height: 34px; border-radius: 50%; }
  .social.one { left: 831px; background: #0a74b3; }
  .social.two { left: 874px; background: #1da1e0; }
</style>
</head>
<body>
  <div class="hero" role="img" aria-label="Dimly lit photograph of a wooden judge's gavel on its sound block"></div>
  <h1 class="hero-title">PUBLIC LAW</h1>
  <div class="hero-rule"></div>

  <header class="topbar"></header>
  <a class="nav-link dim" style="left:28px">Profile</a>
  <a class="nav-link dim" style="left:125px">Projects</a>
  <a class="nav-link light" style="left:241px">Publications</a>
  <div class="brand"><span class="brand-dot"></span><span class="brand-name">Tobias Wenger</span></div>
  <a class="nav-link light" style="left:601px">Courses</a>
  <a class="nav-link light" style="left:712px">Collaborate</a>
  <a class="nav-link light" style="left:858px">Contact</a>

  <p class="copy" style="top:636px">Lorem ipsum dolor sit amet, consectetur adipiscing elit, sed do<br>eiusmod tempor incididunt ut labore et dolore magna aliqua.<br>Ut enim ad minim veniam, quis nostrud exercitation ullamco laboris<br>nisi aliquip ex ea commodo consequat. Duis aute irure dolor in reprehenderit<br>cupidatat non proident, sunt in culpa qui officia deserunt mollit anim id est laborum.</p>

  <h2 class="section-title">SOLUTION</h2>

  <p class="copy" style="top:875px">Lorem ipsum dolor sit amet, consectetur adipiscing elit, sed do<br>eiusmod tempor incididunt ut labore et dolore magna aliqua.<br>Ut enim ad minim veniam, quis nostrud exercitation ullamco laboris<br>aliquip ex ea commodo consequat. Duis aute irure dolor in reprehenderit<br>non proident, sunt in culpa qui officia deserunt mollit anim id est laborum.</p>

  <div class="load-more">LOAD MORE
    <svg width="26" height="14" viewBox="0 0 26 14"><path d="M1 1 L13 12 L25 1" fill="none" stroke="#111" stroke-width="2.6"/></svg>
  </div>

  <footer class="footer">
    <p class="footer-note">Copyright Tobias Wenger 2017</p>
    <span class="social one"></span>
    <span class="social two"></span>
  </footer>
</body>
</html>
```